I need a business card for ALVA Holdings. We are a young startup based in New Zealand working in internet marketing and web development. The design should have some element connected to New Zealand, such as wave, koru or silver fern, just don't use a kiwi bird.

```html
<!DOCTYPE html>
<html lang="en">
<head>
<meta charset="utf-8">
<title>ALVA Holdings – Business Card</title>
<link href="https://fonts.googleapis.com/css2?family=Jost:wght@400;500;600&display=swap" rel="stylesheet">
<style>
  :root {
    --backdrop: #2b2b2b;
    --orange: #f15a24;
    --blue: #0b6fbd;
    --blue-soft: #5aa3dd;
    --ink: #4a4a4a;
    --paper: #ffffff;
  }
  * { margin: 0; padding: 0; box-sizing: border-box; }
  html, body { width: 1200px; height: 768px; overflow: hidden; }
  body {
    background: var(--backdrop);
    font-family: "Jost", sans-serif;
    display: flex;
    align-items: center;
    justify-content: center;
    gap: 48px;
  }
  .card {
    position: relative;
    width: 520px;
    height: 300px;
    border-radius: 22px;
    overflow: hidden;
    box-shadow: 0 14px 30px rgba(0,0,0,0.45);
  }
  .card-back { background: var(--orange); }
  .card-front { background: var(--paper); }

  .back-mark {
    position: absolute;
    left: 50%; top: 112px;
    transform: translate(-50%, -50%);
    display: flex; align-items: center; gap: 14px;
    white-space: nowrap;
  }
  .back-mark .dot {
    width: 30px; height: 30px; border-radius: 50%;
    background: var(--paper);
  }
  .back-mark .name {
    color: var(--paper);
    font-weight: 500;
    font-size: 34px;
    line-height: 1;
    letter-spacing: 1px;
  }
  .back-url {
    position: absolute;
    left: 0; right: 0; bottom: 40px;
    text-align: center;
    color: var(--paper);
    font-size: 13px;
    letter-spacing: 6px;
  }
  .back-wave {
    position: absolute;
    left: 0; top: 0;
    width: 520px; height: 300px;
  }

  .front-logo {
    position: absolute;
    left: 34px; top: 30px;
    display: flex; align-items: center; gap: 12px;
    white-space: nowrap;
  }
  .front-logo .name {
    color: var(--blue);
    font-weight: 600;
    font-size: 36px;
    line-height: 1;
  }
  .front-logo .dot {
    width: 26px; height: 26px; border-radius: 50%;
    background: var(--blue);
  }
  .details {
    position: absolute;
    left: 34px; top: 104px;
    color: var(--ink);
    white-space: nowrap;
  }
  .person {
    color: var(--blue);
    font-weight: 600;
    font-size: 20px;
    line-height: 1;
  }
  .role {
    color: var(--orange);
    font-weight: 500;
    font-size: 14px;
    margin-top: 3px;
  }
  .address {
    font-size: 14px;
    line-height: 1.3;
    margin-top: 12px;
  }
  .contacts { list-style: none; margin-top: 12px; font-size: 14px; line-height: 1.45; }
  .contacts li { display: flex; align-items: center; gap: 8px; }
  .contacts svg { width: 12px; height: 12px; fill: var(--blue); flex: none; }
  .front-waves {
    position: absolute;
    left: 0; top: 0;
    width: 520px; height: 300px;
  }
</style>
</head>
<body>
  <section class="card card-back">
    <svg class="back-wave" viewBox="0 0 520 300" aria-hidden="true">
      <path d="M0 250 C 90 215, 170 285, 260 250 S 430 215, 520 250" fill="none" stroke="var(--paper)" stroke-opacity="0.35" stroke-width="3"/>
    </svg>
    <div class="back-mark">
      <span class="dot"></span>
      <span class="name">ALVA Holdings</span>
    </div>
    <p class="back-url">www.alvaholdings.com</p>
  </section>

  <section class="card card-front">
    <svg class="front-waves" viewBox="0 0 520 300" aria-hidden="true">
      <path d="M250 300 C 310 262, 360 292, 410 250 S 480 170, 520 150 L520 300 Z" fill="var(--blue)"/>
      <path d="M270 262 C 330 228, 370 252, 418 212 S 480 130, 520 112" fill="none" stroke="var(--blue-soft)" stroke-width="8" stroke-linecap="round"/>
      <path d="M300 232 C 350 204, 385 220, 425 184 S 480 100, 520 80" fill="none" stroke="var(--blue)" stroke-width="4" stroke-linecap="round"/>
    </svg>

    <div class="front-logo">
      <span class="name">ALVA Holdings</span>
      <span class="dot"></span>
    </div>

    <div class="details">
      <p class="person">MARA ELLISON</p>
      <p class="role">CEO/FOUNDER</p>
      <p class="address">1420 Harbour View Road<br>Wellington, New Zealand 6011</p>
      <ul class="contacts">
        <li><svg viewBox="0 0 12 12"><path d="M2.5 0.5l2 2.2-1 1.3a7 7 0 0 0 4.5 4.5l1.3-1 2.2 2-1.3 2C5 11 1 7 0.5 1.8z"/></svg>021 555 0193</li>
        <li><svg viewBox="0 0 12 12"><path d="M0 2h12v8H0z M0.8 2.6L6 6.6l5.2-4H0.8z" fill-rule="evenodd"/></svg>mara@alvaholdings.com</li>
        <li><svg viewBox="0 0 12 12"><circle cx="6" cy="6" r="5.5"/><path d="M0.5 6h11M6 0.5c-3 3-3 8 0 11M6 0.5c3 3 3 8 0 11" stroke="#fff" stroke-width="0.8" fill="none"/></svg>www.alvaholdings.com</li>
      </ul>
    </div>
  </section>
</body>
</html>
```